6 - 8 'Holistic' Instagram Graphics

Hi there!
We are looking to build up a library of Graphic Templates to use as Instagram & Facebook posts for our Holistic Medi Spa (& 3 other companies eventually)
This competition is for a sample of 6 - 8 designs. For the winner(s), we will make an agreement for a batch order (Looking for 200+ designs in total), and will be looking to make a long term arrangement.
Please find a full job description in the attached Word Document.
Any questions, don't hesitate to ask.
Thanks!
Medical Spa

```html
<!DOCTYPE html>
<html lang="en">
<head>
<meta charset="utf-8">
<title>Holistic Spa Instagram Posts</title>
<link rel="stylesheet" href="https://fonts.googleapis.com/css2?family=Lato:ital,wght@0,400;1,400;1,900&family=Playfair+Display:ital,wght@0,700;1,400&display=swap">
<style>
  :root {
    --page: #f2f2f2;
    --frame: #ffffff;
    --sky: #8fcde3;
    --sky-veil: rgba(150, 212, 232, 0.72);
    --navy-ink: #1f3550;
    --mint-bg: #e8f7f3;
    --mint-band: #c5ede6;
    --gold: #c5961b;
    --royal: #3a5bc9;
    --teal: #6cc2bb;
    --teal-veil: rgba(108, 180, 176, 0.55);
    --pale-mint: #9af0e0;
    --white: #ffffff;
  }
  * { box-sizing: border-box; margin: 0; padding: 0; }
  html, body { width: 1200px; height: 848px; overflow: hidden; }
  body { background: var(--page); position: relative; font-family: "Lato", sans-serif; }

  .post-frame {
    position: absolute; top: 240px;
    width: 310px; height: 310px; padding: 12px;
    background: var(--frame);
  }
  .post-frame--garden { left: 115px; }
  .post-frame--sunday { left: 458px; }
  .post-frame--living { left: 801px; }

  .post { position: relative; width: 286px; height: 286px; overflow: hidden; }
  .post svg { position: absolute; inset: 0; width: 100%; height: 100%; display: block; }
  .photo-fill { position: absolute; }

  /* Post 1 */
  .garden-photo {
    inset: 0;
    background: linear-gradient(135deg, #d9d4ce 0%, #efece8 35%, #bfc6c9 65%, #a9a4a0 100%);
  }
  .garden-edge { position: absolute; left: 0; top: 0; width: 8px; height: 100%; background: var(--sky); }
  .garden-panel {
    position: absolute; right: 0; top: 0; width: 128px; height: 100%;
    background: var(--sky-veil);
    border-left: 1px dashed rgba(255,255,255,0.8);
    border-bottom: 1px dashed rgba(255,255,255,0.8);
    text-align: center;
  }
  .garden-kicker {
    margin-top: 12px; font-style: italic; font-size: 9px; letter-spacing: 0.5px;
    color: var(--navy-ink);
  }
  .garden-quote {
    margin-top: 10px; font-family: "Playfair Display", serif; font-weight: 700;
    font-size: 23px; line-height: 28px; color: var(--white);
  }

  /* Post 2 */
  .sunday-bg { position: absolute; inset: 0; background: var(--mint-bg); }
  .sunday-title {
    position: absolute; left: 175px; top: 14px;
    font-style: italic; font-weight: 900; font-size: 21px; line-height: 24px;
    color: var(--gold);
  }
  .sunday-cta {
    position: absolute; left: 147px; top: 236px;
    font-style: italic; font-size: 11px; line-height: 14px; color: var(--royal);
  }

  /* Post 3 */
  .living-photo {
    inset: 0;
    background: linear-gradient(160deg, #b9cfcf 0%, #d8d2cc 45%, #b89f94 75%, #8d7c78 100%);
  }
  .living-kicker {
    position: absolute; left: 29px; top: 22px;
    font-size: 12px; letter-spacing: 0.3px; color: var(--pale-mint);
  }
  .living-title {
    position: absolute; left: 10px; top: 40px;
    font-family: "Playfair Display", serif; font-style: italic;
    font-size: 38px; line-height: 42px; color: var(--white);
  }
  .living-title span { display: block; padding-left: 30px; }
</style>
</head>
<body>

  <section class="post-frame post-frame--garden">
    <div class="post">
      <div class="photo-fill garden-photo" role="img" aria-label="Photo of a smiling therapist giving a facial treatment to a client lying on a spa bed"></div>
      <div class="garden-edge"></div>
      <div class="garden-panel">
        <p class="garden-kicker">REMEMBER</p>
        <h2 class="garden-quote">Our<br>bodies<br>are<br>gardens</h2>
      </div>
    </div>
  </section>

  <section class="post-frame post-frame--sunday">
    <div class="post">
      <div class="sunday-bg"></div>
      <svg viewBox="0 0 300 300" aria-hidden="false">
        <polygon points="0,150 128,150 168,300 0,300" fill="var(--mint-band)"/>
        <polygon points="150,300 300,300 300,210 200,210" fill="var(--mint-band)" opacity="0.6"/>
        <g role="img" aria-label="Photo of a microneedling pen being used on a client's face">
          <polygon points="0,0 165,0 178,80 150,148 0,148" fill="#b9a9a3"/>
        </g>
        <g role="img" aria-label="Photo of a client wearing a pink face mask">
          <polygon points="15,207 47,148 112,148 145,207 112,270 47,270" fill="#c69a9a"/>
        </g>
        <g role="img" aria-label="Photo of gloved hands scooping cream from a dark skincare jar">
          <polygon points="125,152 162,82 248,82 287,152 248,224 162,224" fill="#c9d3d0"/>
        </g>
      </svg>
      <h2 class="sunday-title">SELF-CARE<br>SUNDAY!</h2>
      <p class="sunday-cta">USE #BEAUTYSUNDAY<br>JOIN IN!</p>
    </div>
  </section>

  <section class="post-frame post-frame--living">
    <div class="post">
      <div class="photo-fill living-photo" role="img" aria-label="Photo of a client receiving an oxygen spray facial with eyes closed"></div>
      <svg viewBox="0 0 300 300" aria-hidden="true">
        <polygon points="0,0 300,0 300,150 0,150" fill="var(--teal-veil)"/>
        <polygon points="215,0 300,0 300,150 160,150" fill="rgba(255,255,255,0.15)"/>
        <polygon points="45,290 262,290 258,300 48,300" fill="var(--teal)"/>
      </svg>
      <p class="living-kicker">HAPPY HEART</p>
      <h2 class="living-title">Healthy<span>living</span></h2>
    </div>
  </section>

</body>
</html>
```